Business card design needed

I need a business card that sets my business apart from big gyms and intimidating personal trainers. My personal training business focuses on outdoor and client in-home training, in an environment that is both enjoyable and sustainable for the client.
I train males and females, however a large proportion of my clientelle are female, so I would like the card to lean towards females, but still have a bit of masculine appeal about it.
My business colours are a deep sky blue and lightish red/orange (as seen in logo)

Contact Information for Business Card

Trailside Wellness Coaching
Discover a happier, healthier you!
Benedict Harlow- Health and Fitness Professional
Locations all across the Yarra Valley and Eastern Suburbs of Melbourne
0498315260
benedictharlowpt@quillmail.com.au

Requirements
Must have
• - Mobile number must stand out
- The 'Locations all across the Yarra Valley and Eastern Suburbs of Melbourne' must be clear and easy to read (different colour maybe?)

```html
<!DOCTYPE html>
<html lang="en">
<head>
<meta charset="utf-8">
<title>Benedict Harlow – Business Card</title>
<link rel="stylesheet" href="https://fonts.googleapis.com/css2?family=Fira+Sans:ital,wght@0,300;0,600;0,700;1,300;1,400&display=swap">
<style>
  :root {
    --sky-deep: #1a8cf8;
    --sky-mid: #34c4fb;
    --sky-light: #62f6ff;
    --brand-blue: #2f7fe6;
    --accent-red: #f42f0c;
    --white: #ffffff;
  }
  html, body {
    margin: 0;
    padding: 0;
    width: 1200px;
    height: 693px;
    overflow: hidden;
    background: var(--white);
  }
  .card {
    position: relative;
    width: 1200px;
    height: 693px;
    overflow: hidden;
    font-family: "Fira Sans", Arial, sans-serif;
    color: var(--white);
    background:
      radial-gradient(ellipse 780px 620px at 720px 40px, var(--sky-light) 0%, var(--sky-mid) 45%, var(--sky-deep) 100%);
  }
  .business-name {
    position: absolute;
    right: 80px;
    top: 150px;
    margin: 0;
    display: flex;
    align-items: center;
    gap: 22px;
    font-size: 58px;
    font-weight: 700;
    line-height: 1;
    color: var(--brand-blue);
  }
  .business-dot {
    width: 40px;
    height: 40px;
    border-radius: 50%;
    background: var(--white);
    flex: none;
  }
  .tagline {
    position: absolute;
    right: 80px;
    top: 252px;
    margin: 0;
    font-size: 40px;
    font-style: italic;
    font-weight: 400;
    letter-spacing: 3.5px;
    color: var(--accent-red);
  }
  .contact {
    position: absolute;
    right: 92px;
    top: 352px;
    text-align: right;
  }
  .person-name {
    margin: 0;
    font-size: 66px;
    font-weight: 300;
    line-height: 1;
    letter-spacing: 0.5px;
  }
  .person-name strong { font-weight: 600; }
  .person-role {
    margin: 2px 0 0;
    font-size: 32px;
    font-style: italic;
    font-weight: 300;
  }
  .email {
    margin: 40px 0 0;
    font-size: 30px;
    font-style: italic;
    font-weight: 300;
  }
  .phone {
    margin: 4px 0 0;
    font-size: 32px;
    font-weight: 600;
    letter-spacing: 0.5px;
  }
  .locations {
    position: absolute;
    left: 0;
    right: 0;
    bottom: 20px;
    margin: 0;
    text-align: center;
    font-size: 32.5px;
    font-style: italic;
    font-weight: 300;
  }
</style>
</head>
<body>
  <main class="card">
    <h1 class="business-name">
      <span class="business-dot" aria-hidden="true"></span>
      <span>Trailside Wellness Coaching</span>
    </h1>
    <p class="tagline">Discover a happier, healthier you!</p>

    <section class="contact">
      <p class="person-name">BENEDICT <strong>HARLOW</strong></p>
      <p class="person-role">Health and Fitness Professional</p>
      <p class="email">benedictharlowpt@quillmail.com.au</p>
      <p class="phone">0498315260</p>
    </section>

    <p class="locations">locations all across the Yarra Valley and Eastern Suburbs of Melbourne</p>
  </main>
</body>
</html>
```